Marta Business Card

My wife is going to start her own business with renting holiday appartments to tourists. She needs a design for a new business card... and a new web site.
Look at Stayvolt "Erholung auf dem Lindenwäldchen"

Target Market(s)

Give business card to prospects at any situation

Contact Information for Business Card

not sure what this means

Font styles to use
Script

Colors
fec41a
fee18a

Requirements
Must have
• My wife's handwriting is difficult to read:
Entspannen - Loslassen - Auftanken
Marta & das Lindenwäldchen
Urlaub an einem besonderen Ort
Marta Brecke
Grauer Pfad 7
18471 Alt Feldow
post@marta-brecke.de
www.lindenwaeldchen.net
Nice to have
• Beige background
Font like handwriting

```html
<!DOCTYPE html>
<html lang="de">
<head>
<meta charset="utf-8">
<title>Marta Brecke – Visitenkarte</title>
<link rel="stylesheet" href="https://fonts.googleapis.com/css2?family=Courgette&family=Raleway:wght@700&family=Roboto:wght@400&display=swap">
<style>
  :root {
    --backdrop: #d9d0c7;
    --card: #fafafa;
    --navy: #1e3157;
    --grey: #6d7076;
  }
  html, body {
    margin: 0;
    width: 1200px;
    height: 800px;
    overflow: hidden;
    background: var(--backdrop);
  }
  .stage {
    width: 1200px;
    height: 800px;
    display: flex;
    align-items: center;
    justify-content: center;
  }
  .business-card {
    position: relative;
    width: 900px;
    height: 520px;
    background: var(--card);
    box-shadow: 0 6px 24px rgba(60, 45, 30, 0.18);
    box-sizing: border-box;
  }
  .slogan {
    position: absolute;
    top: 70px;
    left: 170px;
    width: 680px;
    margin: 0;
    font-family: "Courgette", cursive;
    font-weight: 400;
    color: var(--navy);
  }
  .slogan-line {
    display: block;
    font-size: 44px;
    line-height: 1.08;
    white-space: nowrap;
  }
  .slogan-line--sub {
    padding-left: 70px;
  }
  .tagline {
    position: absolute;
    top: 186px;
    left: 222px;
    margin: 0;
    font-family: "Roboto", sans-serif;
    font-size: 27px;
    color: var(--grey);
    white-space: nowrap;
  }
  .identity {
    position: absolute;
    top: 322px;
    right: 490px;
    text-align: left;
  }
  .identity-name {
    margin: 0;
    font-family: "Raleway", sans-serif;
    font-weight: 700;
    font-size: 32px;
    letter-spacing: 0.5px;
    color: var(--navy);
    text-transform: uppercase;
    white-space: nowrap;
  }
  .identity-role {
    margin: 2px 0 0 6px;
    font-family: "Roboto", sans-serif;
    font-size: 24px;
    color: var(--grey);
    white-space: nowrap;
  }
  .divider {
    position: absolute;
    top: 322px;
    left: 440px;
    width: 2px;
    height: 160px;
    background: var(--navy);
  }
  .contact {
    position: absolute;
    top: 322px;
    left: 468px;
    margin: 0;
    padding: 0;
    list-style: none;
    font-family: "Roboto", sans-serif;
    font-size: 24px;
    line-height: 31px;
    color: var(--grey);
  }
  .contact-address {
    padding-left: 30px;
  }
  .contact-item {
    display: flex;
    align-items: center;
    gap: 8px;
    color: var(--navy);
  }
  .contact-icon {
    width: 22px;
    height: 22px;
    flex: none;
    fill: var(--navy);
  }
</style>
</head>
<body>
<main class="stage">
  <article class="business-card">
    <h1 class="slogan">
      <span class="slogan-line">Entspannen - Loslassen - Auftanken</span>
      <span class="slogan-line slogan-line--sub">Marta &amp; das Lindenwäldchen</span>
    </h1>
    <p class="tagline">Urlaub an einem besonderen Ort</p>

    <div class="identity">
      <p class="identity-name">Marta Brecke</p>
      <p class="identity-role">Managing Director</p>
    </div>

    <div class="divider"></div>

    <ul class="contact">
      <li class="contact-address">Grauer Pfad 7</li>
      <li class="contact-address">18471 Alt Feldow</li>
      <li class="contact-item">
        <svg class="contact-icon" viewBox="0 0 24 24" aria-hidden="true"><path d="M6.6 2.5l3 3.2-1.8 2.6c1 2.4 3 4.6 5.6 6l2.5-1.9 3.3 3-1.6 3.6C11 18.6 5.4 13 3.1 4.1z"/></svg>
        <span>+56917306422</span>
      </li>
      <li class="contact-item">
        <svg class="contact-icon" viewBox="0 0 24 24" aria-hidden="true"><path d="M2 5h20v14H2z M3.5 6.5L12 13l8.5-6.5" fill="var(--navy)" stroke="var(--card)" stroke-width="1.4"/></svg>
        <span>post@marta-brecke.de</span>
      </li>
      <li class="contact-item">
        <svg class="contact-icon" viewBox="0 0 24 24" aria-hidden="true"><g fill="none" stroke="var(--navy)" stroke-width="1.8"><circle cx="12" cy="12" r="9.5"/><ellipse cx="12" cy="12" rx="4" ry="9.5"/><path d="M2.5 12h19M4 7h16M4 17h16"/></g></svg>
        <span>www.lindenwaeldchen.net</span>
      </li>
    </ul>
  </article>
</main>
</body>
</html>
```